Rollway Stays

We are 100% online, promoting accommodation details and booking facilities for wheelchair dependant travellers.
Listings will only be accommodation providers which meet our specific criteria.

Target Market(s)

Wheelchair dependant people and their companions

Industry/Entity Type

Accommodation

Contact Information for Business Card

Name, mobile phone number, email address, website address

```html
<!DOCTYPE html>
<html lang="en">
<head>
<meta charset="utf-8">
<title>Rollway Stays – Business Card</title>
<link href="https://fonts.googleapis.com/css2?family=Exo+2:wght@400;600;700&display=swap" rel="stylesheet">
<style>
  :root {
    --brand-blue: #00adef;
    --card-white: #ffffff;
    --outline-grey: #6d6e71;
    --text-grey: #5b5b5b;
    --backdrop: #3a3a3c;
  }
  * { margin: 0; padding: 0; box-sizing: border-box; }
  html, body {
    width: 1200px; height: 1018px; overflow: hidden;
    background: var(--backdrop);
    font-family: "Exo 2", Arial, sans-serif;
  }
  .sheet {
    width: 1200px; height: 1018px;
    display: flex; flex-direction: column;
    align-items: center; justify-content: center; gap: 40px;
  }
  .card {
    position: relative; width: 800px; height: 457px; overflow: hidden;
    box-shadow: 0 6px 18px rgba(0,0,0,.35);
  }
  .card-shapes { position: absolute; inset: 0; }

  /* back side */
  .card--back { background: var(--brand-blue); }
  .card--back .brand-name {
    position: absolute; left: 120px; top: 196px;
  }
  .web-strip {
    position: absolute; left: 712px; top: 250px; width: 44px; height: 180px;
    background: var(--card-white);
    display: flex; align-items: center; justify-content: center;
  }
  .web-strip span {
    transform: rotate(-90deg); white-space: nowrap;
    font-size: 15px; letter-spacing: .5px; color: var(--text-grey);
  }

  /* shared brand name */
  .brand-name {
    font-size: 42px; font-weight: 700; letter-spacing: 3px;
    text-transform: uppercase; color: var(--brand-blue);
  }

  /* front side */
  .card--front { background: var(--card-white); }
  .card--front .brand-name { position: absolute; left: 40px; top: 26px; }
  .contact-block {
    position: absolute; right: 40px; top: 150px; width: 340px;
    color: var(--card-white); text-align: right;
  }
  .contact-rule { height: 2px; background: var(--card-white); margin-left: 40px; margin-bottom: 12px; }
  .person-name { font-size: 26px; font-weight: 600; letter-spacing: 2px; text-transform: uppercase; }
  .person-role { font-size: 16px; letter-spacing: 2px; text-transform: uppercase; margin-bottom: 14px; }
  .contact-list { list-style: none; }
  .contact-list li {
    display: flex; justify-content: flex-end; align-items: center; gap: 10px;
    font-size: 14px; letter-spacing: .5px; height: 29px;
  }
  .contact-icon { width: 22px; height: 22px; flex: none; }
</style>
</head>
<body>
<main class="sheet">

  <section class="card card--back" aria-label="Card back">
    <svg class="card-shapes" viewBox="0 0 800 457" aria-hidden="true">
      <path d="M0,58 H540 A170,170 0 0 1 540,398 H0 Z" fill="var(--card-white)"/>
    </svg>
    <div class="brand-name">Rollway Stays</div>
    <div class="web-strip"><span>www.rollwaystays.com</span></div>
  </section>

  <section class="card card--front" aria-label="Card front">
    <svg class="card-shapes" viewBox="0 0 800 457" aria-hidden="true">
      <path d="M800,100 H452 A178,178 0 0 0 452,457 H800 Z" fill="var(--outline-grey)"/>
      <path d="M800,108 H466 A174.5,174.5 0 0 0 466,457 H800 Z" fill="var(--brand-blue)"/>
    </svg>
    <div class="brand-name">Rollway Stays</div>

    <div class="contact-block">
      <div class="contact-rule"></div>
      <div class="person-name">Daniel Reyes</div>
      <div class="person-role">General Manager</div>
      <ul class="contact-list">
        <li>012 555 0147
          <svg class="contact-icon" viewBox="0 0 22 22" aria-hidden="true"><circle cx="11" cy="11" r="10" fill="none" stroke="#fff" stroke-width="1.5"/><path d="M7.5 6.5 l2 -0.5 1 2.5 -1.2 1 a6 6 0 0 0 3 3 l1 -1.2 2.5 1 -0.5 2 c-4 0.5 -8.3 -3.8 -7.8 -7.8z" fill="#fff"/></svg>
        </li>
        <li>012 555 0148
          <svg class="contact-icon" viewBox="0 0 22 22" aria-hidden="true"><circle cx="11" cy="11" r="10" fill="none" stroke="#fff" stroke-width="1.5"/><rect x="8" y="5.5" width="6" height="11" rx="1" fill="none" stroke="#fff" stroke-width="1.4"/><circle cx="11" cy="14.5" r=".8" fill="#fff"/></svg>
        </li>
        <li>daniel@rollwaystays.com
          <svg class="contact-icon" viewBox="0 0 22 22" aria-hidden="true"><circle cx="11" cy="11" r="10" fill="none" stroke="#fff" stroke-width="1.5"/><rect x="6" y="7.5" width="10" height="7" fill="none" stroke="#fff" stroke-width="1.3"/><path d="M6 7.5 l5 4 5 -4" fill="none" stroke="#fff" stroke-width="1.3"/></svg>
        </li>
        <li>www.rollwaystays.com
          <svg class="contact-icon" viewBox="0 0 22 22" aria-hidden="true"><circle cx="11" cy="11" r="10" fill="none" stroke="#fff" stroke-width="1.5"/><circle cx="11" cy="11" r="5" fill="none" stroke="#fff" stroke-width="1.3"/><path d="M6 11 h10 M11 6 c-2.5 3 -2.5 7 0 10 M11 6 c2.5 3 2.5 7 0 10" fill="none" stroke="#fff" stroke-width="1"/></svg>
        </li>
        <li>24 Harbour Lane, Unit 3
          <svg class="contact-icon" viewBox="0 0 22 22" aria-hidden="true"><circle cx="11" cy="11" r="10" fill="none" stroke="#fff" stroke-width="1.5"/><path d="M11 17 c-3 -3.5 -4 -5.5 -4 -7 a4 4 0 0 1 8 0 c0 1.5 -1 3.5 -4 7z" fill="#fff"/><circle cx="11" cy="10" r="1.4" fill="var(--brand-blue)"/></svg>
        </li>
      </ul>
    </div>
  </section>

</main>
</body>
</html>
```